A 4 to 5 page business website. Similar to http://featherlinestudio.com

Velora is the premier lash and brow studio in Cincinnati. All services are performed by a licensed esthetician which means the condition of your skin is our top priority. We adhere to all state board and board of cosmetology sanitation standards. Which means we go above and beyond to insure your safety and comfort. Quality services Quality products and Quality customer care. We offer Miscroblading, Micorshading and multiple eyelash extensions.

I would like the website to mimic the colors scheme of my logo I also have a few website's that I would like to be used for inspiration on design.

@Velorabrowz on instagram and Velora Brows on Facebook

Please find attached my logo. I would like it to be at the top of each page along with a "Book Appointment" button that take the user to my scheduling website.

I have also attached some pictures for the Lashes Page and Microblading (before and afters of Microblading).

I also want client reviews/testimonials on the home page if possible near the bottom of the page this is one of them but I have more at www.studiokornet.com type Marlena Odefy into the search bar

This is two websites that I liked the look and feel of for inspiration:
www.featherlinestudio.com | I like the look and feel of this website
www.quillwink.net | I like the scrolling pictures on this websites home page

Target Market(s)

Women age 18 to 60

Industry/Entity Type

Beauty Salon

Number of Pages Required

5+ page

Requirements
Must have
• The stock photos should be women of different ethnicities (for example one white, One black ect)

```html
<!DOCTYPE html>
<html lang="en">
<head>
<meta charset="utf-8">
<title>Velora Brows – Lash and Brow Studio</title>
<link rel="stylesheet" href="https://fonts.googleapis.com/css2?family=Oswald:wght@300;400;500&family=Open+Sans:wght@400;600&family=Dancing+Script:wght@500&display=swap">
<style>
:root{
  --blue:#4fb4e0;
  --blue-btn:#66c4ea;
  --peach:#f7c594;
  --orange:#f0a23a;
  --ink:#222;
  --text:#555;
  --grey-band:#d6d6d6;
  --grey-soft:#ececec;
  --dark:#2b2b2b;
  --white:#fff;
}
*{margin:0;padding:0;box-sizing:border-box}
html,body{width:1200px;height:3945px;overflow:hidden}
body{position:relative;font-family:"Open Sans",Arial,sans-serif;color:var(--text);background:var(--white)}
section,header,footer{position:absolute;left:0;width:1200px;overflow:hidden}
.script{font-family:"Dancing Script",cursive;font-weight:500;text-transform:none}
.heading{font-family:"Oswald",Arial,sans-serif;font-weight:400;text-transform:uppercase;color:var(--ink);font-size:26px;line-height:40px;text-align:center;letter-spacing:.5px}
.heading .script{font-size:32px;margin-left:8px}
.btn{position:absolute;display:flex;align-items:center;justify-content:center;font-family:"Oswald",Arial,sans-serif;font-size:15px;text-decoration:none}
.btn-dark{background:#0d0d0d;color:var(--white)}
.photo{position:absolute}

/* hero */
.hero{top:0;height:645px}
.hero .photo{inset:0;background:linear-gradient(100deg,#c9b59c 0%,#8e7763 30%,#5e4a3e 55%,#3a2f2a 75%,#a98f74 100%)}
.hero .shade{position:absolute;left:0;top:0;width:1200px;height:150px;background:linear-gradient(rgba(0,0,0,.55),rgba(0,0,0,0))}
.logo{position:absolute;left:118px;top:76px;font-family:"Oswald",Arial,sans-serif;font-weight:400;font-size:44px;line-height:52px;color:var(--blue);letter-spacing:1px}
.phone{position:absolute;left:876px;top:24px;font-family:"Oswald",Arial,sans-serif;font-size:16px;line-height:22px;color:var(--white)}
.social{position:absolute;top:22px;width:24px;height:24px;background:var(--orange)}
.book-top{left:390px;top:84px;width:131px;height:32px;background:var(--peach);color:var(--ink);font-size:14px}
.nav{position:absolute;left:592px;top:90px;display:flex;gap:30px;list-style:none}
.nav li{font-family:"Oswald",Arial,sans-serif;font-weight:300;font-size:15px;line-height:20px;color:var(--white)}
.tagline{position:absolute;top:298px;width:1200px;text-align:center;font-family:"Oswald",Arial,sans-serif;font-size:22px;line-height:30px;color:var(--white);letter-spacing:.5px}
.know{left:500px;top:358px;width:197px;height:44px;background:var(--blue-btn);color:var(--ink)}

/* about */
.about{top:645px;height:329px;background:var(--white)}
.about .heading{margin-top:86px;color:var(--blue)}
.body-copy{width:850px;margin:24px auto 0;text-align:center;font-size:14px;line-height:24px;color:#444}

/* microblading */
.micro{top:974px;height:468px;background:var(--grey-band)}
.micro .photo{inset:0;background:linear-gradient(90deg,#ebebeb 0%,#cfcfcf 45%,#b8b8b8 75%,#c8c8c8 100%)}
.micro .heading{position:relative;margin-top:98px}
.micro .body-copy{position:relative;width:820px;margin-top:22px}
.micro .body-copy p+p{margin-top:12px}
.learn{left:522px;top:330px;width:156px;height:46px}

/* reviews */
.reviews{top:1442px;height:435px;background:var(--grey-soft)}
.reviews .heading{margin-top:104px;color:var(--blue)}
.quote{width:830px;margin:18px auto 0;text-align:center;font-size:14px;line-height:25px;color:#444}
.author{text-align:center;margin-top:12px;font-size:13px;line-height:20px;color:#444}
.arrow{position:absolute}
.dots{position:absolute;left:566px;top:320px;display:flex;gap:8px}
.dots i{width:16px;height:16px;background:#999;display:block}
.dots i:first-child{background:var(--blue)}

/* services */
.services{top:1877px;height:413px}
.services .photo{inset:0;background:linear-gradient(90deg,#d9d9d9 0%,#c9c9c9 40%,#a9a9a9 70%,#cdcdcd 100%)}
.services .heading{position:relative;margin-top:92px}
.service-list{position:absolute;top:190px;left:160px;width:880px;display:flex;justify-content:space-between;list-style:none}
.service-list li{font-family:"Oswald",Arial,sans-serif;font-size:18px;line-height:22px;color:var(--ink);text-align:center;width:150px}
.book-now{left:527px;top:293px;width:145px;height:44px}

/* blog */
.blog{top:2290px;height:731px;background:var(--white)}
.blog .heading{margin-top:70px}
.post{position:absolute;top:171px;width:228px}
.post .photo{position:relative;width:228px;height:182px;background:linear-gradient(135deg,#7a5a48,#c9a48c 55%,#e8e2dc)}
.date{position:absolute;left:-66px;top:12px;width:66px;height:54px;background:var(--blue);color:var(--ink);font-family:"Oswald",Arial,sans-serif;font-size:14px;line-height:18px;text-align:center;padding-top:8px}
.post h3{font-family:"Open Sans",Arial,sans-serif;font-weight:600;font-size:15px;line-height:22px;color:var(--ink);margin-top:16px}
.meta{font-size:11px;line-height:16px;color:#888;margin-top:12px;display:flex;gap:16px;align-items:center}
.meta b{display:inline-block;width:9px;height:9px;background:var(--orange);margin-right:4px;vertical-align:middle}
.post p{font-size:12px;line-height:19px;color:#666;margin-top:12px}

/* before & after */
.results{top:3021px;height:532px;background:linear-gradient(90deg,#f6dcc4 0%,#f1e9e0 45%,#cfe7f3 100%)}
.results .heading{margin-top:74px}
.panel{position:absolute;top:151px;height:250px;border:2px solid var(--white)}
.p1{left:116px;width:313px;background:linear-gradient(160deg,#c9b6a6,#8d7468 50%,#e4d4c8)}
.p2{left:447px;width:311px;background:linear-gradient(180deg,#8a6a58,#4a3a32 55%,#b49584)}
.p3{left:774px;width:310px;background:linear-gradient(180deg,#d8b9a2,#a07f6b 60%,#e7ddd5)}

/* footer */
.site-footer{top:3553px;height:342px;background:var(--white)}
.map{position:absolute;left:0;top:0;width:584px;height:342px;background:linear-gradient(135deg,#e7ece4,#d8e4ee 50%,#e9ebe3)}
.links{position:absolute;left:614px;top:52px}
.footer-title{font-family:"Oswald",Arial,sans-serif;font-weight:400;font-size:15px;line-height:20px;letter-spacing:.5px;color:var(--ink);text-transform:uppercase;border-bottom:1px solid #bbb;padding-bottom:8px;width:190px}
.links ul{list-style:none;margin-top:14px}
.links li{font-size:13px;line-height:24px;color:#444}
.links li::before{content:"";display:inline-block;width:6px;height:6px;background:var(--ink);border-radius:50%;margin-right:8px;vertical-align:middle}
.contact{position:absolute;left:842px;top:0;width:358px;height:342px;background:var(--dark);padding:44px 0 0 26px;color:#ddd}
.contact .footer-title{color:var(--white);border:0;width:auto;padding:0}
.contact-row{display:flex;gap:12px;font-size:12px;line-height:18px;margin-top:16px}
.contact-row svg{flex:none;margin-top:3px}
.contact .connect{margin-top:28px}
.contact .socials{display:flex;gap:16px;margin-top:14px}
.contact .socials i{width:26px;height:26px;background:var(--orange);display:block}
.bottom-bar{top:3895px;height:50px;background:var(--white);font-size:11px;line-height:14px;color:#555}
.bottom-bar span{position:absolute;top:18px}
</style>
</head>
<body>

<header class="hero">
  <div class="photo" role="img" aria-label="Portrait photograph of a woman with defined brows and lashes, resting her chin on her hand, wearing a gold earring"></div>
  <div class="shade"></div>
  <div class="logo">Velora Brows</div>
  <div class="phone">Call 513-555-0142</div>
  <span class="social" style="left:1008px"></span>
  <span class="social" style="left:1042px"></span>
  <a class="btn book-top">Book Appointment</a>
  <ul class="nav">
    <li>Home</li><li>About Us</li><li>Lashes</li><li>Brows</li><li>Blog</li><li>Testimonial</li><li>Contact Us</li>
  </ul>
  <p class="tagline">QUALITY SERVICES QUALITY PRODUCTS AND QUALITY CUSTOMER CARE.</p>
  <a class="btn know">Know more Velora Brows</a>
</header>

<section class="about">
  <h2 class="heading"><span>About</span><span class="script">Velora Brows</span></h2>
  <p class="body-copy">Velora is the premier lash and brow studio in Cincinnati. All services are performed by a licensed esthetician which means the condition of your skin is our top priority. We adhere to all state board and board of cosmetology sanitation standards. Which means we go above and beyond to insure your safety. Comfort is also very high on our list of priority's. Quality services Quality products and Quality customer care.</p>
</section>

<section class="micro">
  <div class="photo" role="img" aria-label="Muted grey photograph of a microblading treatment on a client's brow"></div>
  <h2 class="heading">What is<span class="script">Microblading?</span></h2>
  <div class="body-copy">
    <p>Microblading eyebrows is a form of permanent makeup that creates natural, beautiful eyebrows with a handheld microblade. It's perfect for people who have overplucked or those who want to define, darken or reshape their eyebrows.</p>
    <p>Microblading originated in Asia over 25 years ago and has gone by many names: eyebrow embroidery, feather touch, microstroking and even "the Japanese Method." By 2015, microblading became popular in the United States.</p>
  </div>
  <a class="btn btn-dark learn">Learn More</a>
</section>

<section class="reviews">
  <h2 class="heading">Client<span class="script">Reviews</span></h2>
  <p class="quote">"My eyebrows are on fleek. First time having them microblade. Im so excited that i never have to do anything to them myself i was always messing them up. I will be back Ms.Odefy job well done."</p>
  <p class="author">- Dana R.</p>
  <svg class="arrow" style="left:172px;top:200px" width="22" height="40" viewBox="0 0 22 40"><path d="M19 2 3 20l16 18" fill="none" stroke="#333" stroke-width="3"/></svg>
  <svg class="arrow" style="left:1000px;top:200px" width="22" height="40" viewBox="0 0 22 40"><path d="M3 2l16 18L3 38" fill="none" stroke="#333" stroke-width="3"/></svg>
  <div class="dots"><i></i><i></i><i></i></div>
</section>

<section class="services">
  <div class="photo" role="img" aria-label="Muted grey photograph of eyelash extensions being applied"></div>
  <h2 class="heading">Velora Brows<span class="script">Services</span></h2>
  <ul class="service-list">
    <li>Mink Eyelash<br>Extensions</li>
    <li>Duo Eyelash<br>Extensions</li>
    <li>Luxury Cluser<br>Lashes</li>
    <li>Microblading<br>Simi Permenant</li>
    <li>Microshading<br>3D Ombre'</li>
  </ul>
  <a class="btn btn-dark book-now">Book Now !</a>
</section>

<section class="blog">
  <h2 class="heading">News<span class="script">Blog</span></h2>
  <article class="post" style="left:190px">
    <div class="photo" role="img" aria-label="Close-up photograph of a brow treatment in progress"></div>
    <div class="date">04<br>Nov</div>
    <h3>Donec semper tellus vitae massa scelerisque auctor.</h3>
    <div class="meta"><span><b></b>Admin</span><span><b></b>6</span></div>
    <p>Lorem ipsum dolor sit amet, consectetur adipiscing elit. Mauris vitae mollis arcu. In hac habitasse platea dictumst. Sed rhoncus magna ultrices, dignissim lacus sit amet, consectetur tortor. Vivamus ac dolor efficitur est porta pretium id ac sapien.</p>
  </article>
  <article class="post" style="left:518px">
    <div class="photo" role="img" aria-label="Close-up photograph of a client during a lash treatment"></div>
    <div class="date">23<br>Oct</div>
    <h3>Donec semper tellus vitae massa scelerisque auctor.</h3>
    <div class="meta"><span><b></b>Admin</span><span><b></b>6</span></div>
    <p>Lorem ipsum dolor sit amet, consectetur adipiscing elit. Mauris vitae mollis arcu. In hac habitasse platea dictumst. Sed rhoncus magna ultrices, dignissim lacus sit amet, consectetur tortor. Vivamus ac dolor efficitur est porta pretium id ac sapien. Suspendisse pretium, nulla finibus feugiat consequat, massa tellus condimentum diam, eget iaculis erat urna ut nulla.</p>
  </article>
  <article class="post" style="left:845px">
    <div class="photo" role="img" aria-label="Close-up photograph of a brow treatment in progress"></div>
    <div class="date">04<br>Oct</div>
    <h3>Donec semper tellus vitae massa scelerisque auctor.</h3>
    <div class="meta"><span><b></b>Admin</span><span><b></b>6</span></div>
    <p>Mauris vitae mollis arcu. In hac habitasse platea dictumst. Sed rhoncus magna ultrices, dignissim lacus sit amet, consectetur tortor. Vivamus ac dolor efficitur est porta pretium id ac sapien. Suspendisse pretium, nulla finibus feugiat consequat, massa tellus condimentum diam, eget iaculis erat urna ut nulla.</p>
  </article>
</section>

<section class="results">
  <h2 class="heading">Microblading<span class="script">Before and After</span></h2>
  <svg class="arrow" style="left:58px;top:248px" width="24" height="64" viewBox="0 0 24 64"><path d="M21 2 3 32l18 30" fill="none" stroke="#222" stroke-width="2.5"/></svg>
  <div class="panel p1" role="img" aria-label="Collage of before and after microblading photographs of eyes and brows"></div>
  <div class="panel p2" role="img" aria-label="Before and after photograph of microbladed brows"></div>
  <div class="panel p3" role="img" aria-label="After photograph of a finished microbladed brow"></div>
  <svg class="arrow" style="left:1116px;top:248px" width="24" height="64" viewBox="0 0 24 64"><path d="M3 2l18 30L3 62" fill="none" stroke="#222" stroke-width="2.5"/></svg>
</section>

<footer class="site-footer">
  <div class="map" role="img" aria-label="Street map marking the studio location"></div>
  <div class="links">
    <h4 class="footer-title">Use Full Links</h4>
    <ul><li>Lashes</li><li>Brows</li><li>Blog</li><li>Testimonial</li><li>Contact Us</li></ul>
  </div>
  <div class="contact">
    <h4 class="footer-title">Contact Info</h4>
    <div class="contact-row">
      <svg width="12" height="14" viewBox="0 0 12 14"><path d="M6 0a5 5 0 0 0-5 5c0 4 5 9 5 9s5-5 5-9a5 5 0 0 0-5-5zm0 7a2 2 0 1 1 0-4 2 2 0 0 1 0 4z" fill="#bbb"/></svg>
      <span>Studio Kornet 4120 Alder Ridge Rd<br>Suite #14 Larkfield,<br>Ohio 45099</span>
    </div>
    <div class="contact-row">
      <svg width="12" height="12" viewBox="0 0 12 12"><path d="M2.5 0 5 3 3.6 4.6a7 7 0 0 0 3.8 3.8L9 7l3 2.5L10.5 12A10.5 10.5 0 0 1 0 1.5z" fill="#bbb"/></svg>
      <span>513-555-0142</span>
    </div>
    <div class="contact-row">
      <svg width="12" height="10" viewBox="0 0 12 10"><rect x=".5" y=".5" width="11" height="9" fill="none" stroke="#bbb"/><path d="M.5.5 6 5l5.5-4.5" fill="none" stroke="#bbb"/></svg>
      <span>mlena@velorabrows.com</span>
    </div>
    <h4 class="footer-title connect">Connect With Us</h4>
    <div class="socials"><i></i><i></i></div>
  </div>
</footer>

<footer class="bottom-bar">
  <span style="left:94px">COPYRIGHT © 2017 VELORA BROWS</span>
  <span style="left:955px">HOME | TERMS &amp; POLICIES</span>
</footer>

</body>
</html>
```